Lighting & Automation,Audio services Needs Flyer Design

We need a 2 sided half page flyer. One side is about a specific product service we offer, please visit www.vorquill.com
Pelmora Marketing Materials and Guidelines please visit
http://www.vorquill.com/marketing-materials/
We would like to see design that use the color from our logo and Pelmora colors (Blue). The final design should communicate a message to its audience about the product advantage.
Example: No matter where you are - at home or abroad, you can always control access to your home.
Other Side we need design for our high quality services what include all electrical services. Visit www.dabrune.com or glimvasteroc.com
Please use our logo attached below.

Company Name:
Dabrune
Office 555-274-6137
email info@dabrune.com
Web Dabrune.com

Target Market(s)

Residential Customers-Home Owners

Industry/Entity Type

Professional Service

Font styles to use
Serif

Colors

Designer to choose colors to be used in the design.

Requirements
Must have
• Stand out from the crowd
• Capture Customer attention
Should not have
• Don’t overstuff words

```html
<!DOCTYPE html>
<html lang="en">
<head>
<meta charset="utf-8">
<title>Dabrune Flyer</title>
<link href="https://fonts.googleapis.com/css2?family=Source+Sans+3:wght@400;500;600;700&display=swap" rel="stylesheet">
<style>
  :root{
    --orange:#f7941d;
    --orange-light:#fbae3c;
    --blue-deep:#1565b5;
    --blue-bright:#29a8e0;
    --blue-text:#1d7cc4;
    --ink:#4d4d4d;
    --paper:#ffffff;
    --swoosh:#d6d9de;
    --backdrop:#e9eaec;
  }
  *{box-sizing:border-box;margin:0;padding:0}
  html,body{width:945px;height:1200px;overflow:hidden}
  body{background:var(--backdrop);font-family:"Source Sans 3",Arial,sans-serif;position:relative}
  .flyer{position:absolute;left:80px;width:785px;height:508px;background:var(--paper);overflow:hidden;box-shadow:0 4px 14px rgba(0,0,0,.25)}
  .flyer--front{top:46px}
  .flyer--back{top:620px}
  .band{position:absolute;left:0;width:100%;background:linear-gradient(90deg,var(--orange),var(--orange-light) 60%,var(--orange));color:#fff}
  .band--head{top:0;display:flex;align-items:center;justify-content:center;text-align:center;text-transform:uppercase}
  .flyer--front .band--head{height:68px;font-size:17.5px;font-weight:500;line-height:21px}
  .flyer--back .band--head{height:67px;font-size:26px;font-weight:500;letter-spacing:.3px}
  .band--foot{bottom:0;height:33px;display:flex;align-items:center;font-size:16px;font-weight:500;letter-spacing:.2px}
  .contact{position:absolute;display:flex;align-items:center;gap:8px}
  .contact svg{width:12px;height:12px}
  .contact--mail{left:30px}
  .contact--phone{left:335px}
  .contact--web{right:38px}
  .stage{position:absolute;left:0;width:100%}
  .flyer--front .stage{top:68px;height:408px}
  .flyer--back .stage{top:67px;height:248px}
  .stage svg.art{position:absolute;inset:0;width:100%;height:100%}
  .brand{position:absolute;color:#fff;font-weight:700;font-size:34px;letter-spacing:1px;display:flex;align-items:center;gap:8px}
  .brand::before{content:"";width:14px;height:14px;border-radius:50%;background:#fff}
  .flyer--front .brand{left:22px;top:10px}
  .flyer--back .brand{left:20px;top:14px}
  .headline{position:absolute;left:23px;top:66px;color:#fff;font-weight:600;font-size:21.5px;line-height:31px;text-transform:uppercase}
  .pitch{position:absolute;left:266px;top:294px;width:430px}
  .pitch h2{color:var(--blue-text);font-weight:500;font-size:21px;margin-bottom:8px}
  .pitch p{color:var(--ink);font-size:13px;line-height:17px}
  .intro{position:absolute;left:18px;top:80px;width:222px;color:#fff;font-size:13.6px;line-height:16px}
  .features{position:absolute;top:322px;left:34px;right:10px;list-style:none}
  .features li{display:flex;align-items:center;height:37px;font-size:17px;color:var(--ink);margin-bottom:3px}
  .features li:last-child{margin-top:4px}
  .features svg{width:32px;height:32px;flex:none;margin-right:11px}
  .features b{color:var(--blue-text);font-weight:500;text-transform:uppercase;margin-right:4px}
</style>
</head>
<body>

<section class="flyer flyer--front">
  <header class="band band--head">No matter where you are - at home or abroad,&nbsp; you can always<br>control access to your home.</header>
  <div class="stage">
    <svg class="art" viewBox="0 0 785 408" preserveAspectRatio="none">
      <defs>
        <linearGradient id="houseTone" x1="0" y1="0" x2="1" y2="1">
          <stop offset="0" stop-color="#8c97a8"/><stop offset=".5" stop-color="#a39380"/><stop offset="1" stop-color="#c9a070"/>
        </linearGradient>
        <linearGradient id="wedgeBlue" x1="0" y1="0" x2="1" y2="1">
          <stop offset="0" stop-color="var(--blue-deep)"/><stop offset="1" stop-color="var(--blue-bright)"/>
        </linearGradient>
        <linearGradient id="handTone" x1="0" y1="0" x2="1" y2="1">
          <stop offset="0" stop-color="#e6e9ee"/><stop offset=".5" stop-color="#8fb7dc"/><stop offset="1" stop-color="#e7c5ab"/>
        </linearGradient>
      </defs>
      <rect x="180" y="0" width="605" height="408" fill="url(#houseTone)" role="img" aria-label="Photo of a lit two-storey suburban house at dusk"/>
      <path d="M0,0 L350,0 C300,90 200,190 0,250 Z" fill="var(--swoosh)"/>
      <path d="M0,0 L330,0 C280,90 180,180 0,236 Z" fill="url(#wedgeBlue)"/>
      <path d="M0,408 L0,318 C150,282 330,246 470,252 C610,260 720,330 785,392 L785,408 Z" fill="var(--swoosh)"/>
      <path d="M0,408 L0,328 C150,292 330,258 470,264 C610,272 715,345 785,408 Z" fill="var(--paper)"/>
      <rect x="6" y="138" width="222" height="268" rx="30" fill="url(#handTone)" role="img" aria-label="Hand holding a smartphone showing a home control app"/>
    </svg>
    <div class="brand">Dabrune</div>
    <h1 class="headline">Remotely control<br>your home</h1>
    <div class="pitch">
      <h2>Build a Smarthome</h2>
      <p>Pelmora® transforms the "connected home" from a buzzword into reality. Make life simple by connecting you to the things that matter. Control your lights, alarms, A/C,Cameras,TV's, watering system and many other devices from wherever you are in the world.</p>
    </div>
  </div>
  <footer class="band band--foot">
    <span class="contact contact--mail"><svg viewBox="0 0 12 12"><rect x="0" y="1" width="12" height="10" rx="2" fill="#fff"/><path d="M2,4 L6,7 L10,4" stroke="var(--orange)" stroke-width="1.3" fill="none"/></svg>info@dabrune.com</span>
    <span class="contact contact--phone"><svg viewBox="0 0 12 12"><rect width="12" height="12" rx="2" fill="#fff"/><path d="M3,3 C3,7 5,9 9,9 L9,7.5 L7.5,7 L6.8,7.8 C5.5,7.2 4.8,6.5 4.2,5.2 L5,4.5 L4.5,3 Z" fill="var(--orange)"/></svg>555-274-6137</span>
    <span class="contact contact--web"><svg viewBox="0 0 12 12"><rect width="12" height="12" rx="2" fill="#fff"/><circle cx="6" cy="6" r="3.5" stroke="var(--orange)" stroke-width="1" fill="none"/><path d="M2.5,6 H9.5 M6,2.5 V9.5" stroke="var(--orange)" stroke-width="1"/></svg>www.dabrune.com</span>
  </footer>
</section>

<section class="flyer flyer--back">
  <header class="band band--head">Enjoy remote control</header>
  <div class="stage">
    <svg class="art" viewBox="0 0 785 248" preserveAspectRatio="none">
      <defs>
        <linearGradient id="techTone" x1="0" y1="0" x2="1" y2="0">
          <stop offset="0" stop-color="#c3ccd8"/><stop offset=".6" stop-color="#6f8fb5"/><stop offset="1" stop-color="#b7c6d8"/>
        </linearGradient>
        <linearGradient id="wedgeBlue2" x1="0" y1="0" x2="1" y2="1">
          <stop offset="0" stop-color="var(--blue-bright)"/><stop offset="1" stop-color="var(--blue-deep)"/>
        </linearGradient>
      </defs>
      <rect x="0" y="0" width="785" height="248" fill="url(#techTone)" role="img" aria-label="Photo of a person touching a glowing smart-home icon network"/>
      <path d="M0,0 L395,0 C320,110 190,210 0,248 Z" fill="var(--swoosh)"/>
      <path d="M0,0 L380,0 C300,110 180,195 0,232 Z" fill="url(#wedgeBlue2)"/>
    </svg>
    <div class="brand">Dabrune</div>
    <p class="intro">Dabrune’s Technicians and Master Electricians provide expert service to designers, general contractors, and residential customers.</p>
  </div>
  <ul class="features">
    <li><svg viewBox="0 0 32 32"><circle cx="16" cy="16" r="15" fill="var(--blue-deep)" stroke="#9cc3e6" stroke-width="2"/><path d="M9,14 A10,10 0 0 1 23,14 M11.5,17 A6.5,6.5 0 0 1 20.5,17" stroke="#fff" stroke-width="2" fill="none" stroke-linecap="round"/><circle cx="16" cy="20.5" r="1.8" fill="#fff"/></svg><b>Control</b> - You can control device to change settings, all from your smartphone or tablet.</li>
    <li><svg viewBox="0 0 32 32"><circle cx="16" cy="16" r="15" fill="var(--blue-deep)" stroke="#9cc3e6" stroke-width="2"/><rect x="9" y="10" width="14" height="13" rx="1.5" stroke="#fff" stroke-width="1.8" fill="none"/><path d="M9,14 H23 M12,17.5 L14,19.5 L19,15.5" stroke="#fff" stroke-width="1.6" fill="none"/></svg><b>Automate with schedule</b> - Create customized groups or turn on/off lights various times.</li>
    <li><svg viewBox="0 0 32 32"><circle cx="16" cy="16" r="15" fill="var(--blue-deep)" stroke="#9cc3e6" stroke-width="2"/><circle cx="16" cy="16" r="5.5" stroke="#fff" stroke-width="3" stroke-dasharray="2.4 1.9" fill="none"/><circle cx="16" cy="16" r="2" fill="#fff"/></svg><b>Create scenes</b> - Quickly create scenes that let you control multiple device at the same time.</li>
    <li><svg viewBox="0 0 32 32"><circle cx="16" cy="16" r="15" fill="var(--blue-deep)" stroke="#9cc3e6" stroke-width="2"/><path d="M16,8 L24,22 H8 Z" fill="#fff"/><path d="M16,12.5 V17.5" stroke="var(--blue-deep)" stroke-width="1.8"/><circle cx="16" cy="19.6" r="1" fill="var(--blue-deep)"/></svg><b>Instant alerts</b> - Let Pelmora® be your watchdog.</li>
  </ul>
  <footer class="band band--foot">
    <span class="contact contact--mail"><svg viewBox="0 0 12 12"><rect x="0" y="1" width="12" height="10" rx="2" fill="#fff"/><path d="M2,4 L6,7 L10,4" stroke="var(--orange)" stroke-width="1.3" fill="none"/></svg>info@dabrune.com</span>
    <span class="contact contact--phone"><svg viewBox="0 0 12 12"><rect width="12" height="12" rx="2" fill="#fff"/><path d="M3,3 C3,7 5,9 9,9 L9,7.5 L7.5,7 L6.8,7.8 C5.5,7.2 4.8,6.5 4.2,5.2 L5,4.5 L4.5,3 Z" fill="var(--orange)"/></svg>555-274-6137</span>
    <span class="contact contact--web"><svg viewBox="0 0 12 12"><rect width="12" height="12" rx="2" fill="#fff"/><circle cx="6" cy="6" r="3.5" stroke="var(--orange)" stroke-width="1" fill="none"/><path d="M2.5,6 H9.5 M6,2.5 V9.5" stroke="var(--orange)" stroke-width="1"/></svg>www.dabrune.com</span>
  </footer>
</section>

</body>
</html>
```